Gadgeteer Glowhaus Business Card

we are selling techies and beauties stuffs online and store line.
will be expanding into craft products, specifically handmade products,
therefore i want my name card / business card designs to be crafty , carton box look a like, with colour theme from "bidmarto logo" because that will be our main base of operations, if possible, do a little logo of "visit store" as it looks like from bidmarto, as well as bidmarto logo on the business card. Please as well leave a line for me to stick my website sticker on it once i've got my website set up in the future.
Updates

 i want my business card to have yellowish brown (carton box lookalike) color as a base, while the rest will be based on bidmarto's logo color theme. thank you.

Industry/Entity Type

Store

Contact Information for Business Card

-for your everyday techie and beauty needs -

Gadgeteer Glowhaus

R.J. Morrow
47, Wexcombe Avenue,
Ferndale Heights, Victoria 3187
Australia

Colors
eb1f27
0255a3
fbed22
9bcb3c

Requirements
Must have
• a carton box cut-out lookalike

```html
<!DOCTYPE html>
<html lang="en">
<head>
<meta charset="utf-8">
<title>Gadgeteer Glowhaus Business Card</title>
<link rel="stylesheet" href="https://fonts.googleapis.com/css2?family=Open+Sans:wght@400;600&family=Sniglet&display=swap">
<style>
  :root {
    --backdrop: #e6e1d8;
    --kraft-dark: #8a6231;
    --kraft: #b5854a;
    --kraft-light: #d9b27a;
    --kraft-pale: #ecd3a6;
    --kraft-edge: #6e4c24;
    --ink-dark: #3a2812;
    --ink-light: #fff6e6;
    --brand-red: #eb1f27;
    --brand-blue: #0255a3;
    --brand-yellow: #fbed22;
    --brand-green: #9bcb3c;
  }
  * { box-sizing: border-box; margin: 0; padding: 0; }
  html, body { width: 1200px; height: 1200px; overflow: hidden; }
  body {
    background: var(--backdrop);
    font-family: "Open Sans", Arial, sans-serif;
    position: relative;
  }
  .card {
    position: absolute;
    left: 180px;
    width: 840px;
    height: 480px;
    border-radius: 34px;
    overflow: hidden;
    background:
      repeating-linear-gradient(90deg, rgba(255,255,255,0.04) 0 3px, rgba(0,0,0,0.03) 3px 7px),
      radial-gradient(ellipse at 50% 40%, var(--kraft), var(--kraft-dark) 85%);
    box-shadow: 0 10px 30px rgba(60,40,10,0.35);
  }
  .card--front { top: 80px; }
  .card--back { top: 600px; }

  /* front */
  .front__header {
    position: absolute; left: 0; top: 0; width: 100%; height: 216px;
    background:
      repeating-linear-gradient(90deg, rgba(255,255,255,0.05) 0 3px, rgba(0,0,0,0.025) 3px 7px),
      linear-gradient(180deg, var(--kraft-pale) 0%, var(--kraft-light) 100%);
  }
  .front__band {
    position: absolute; left: 0; top: 216px; width: 100%; height: 20px;
    background: linear-gradient(90deg,
      var(--brand-red) 0 25%, var(--brand-blue) 25% 50%,
      var(--brand-yellow) 50% 75%, var(--brand-green) 75% 100%);
  }
  .brand-dot {
    position: absolute; left: 173px; top: 24px;
    width: 144px; height: 144px; border-radius: 50%;
    background: var(--brand-blue);
  }
  .brand-name {
    position: absolute; left: 382px; top: 80px; width: 300px;
    text-align: center;
    font-family: "Sniglet", "Open Sans", sans-serif;
    font-size: 30px; color: var(--brand-red);
    white-space: nowrap;
  }
  .tagline {
    position: absolute; left: 382px; top: 128px; width: 300px;
    text-align: center; font-size: 21px; line-height: 34px; color: var(--ink-dark);
  }
  .name-tab {
    position: absolute; left: 435px; top: 236px; width: 368px; height: 73px;
    background: linear-gradient(180deg, var(--kraft-light) 0%, var(--kraft-pale) 50%, var(--kraft-light) 100%);
    clip-path: polygon(0 0, 100% 0, 100% 55%, 93% 100%, 8% 100%, 0 55%);
    display: flex; align-items: center; justify-content: center;
  }
  .name-tab__text {
    font-size: 26px; letter-spacing: 52px; margin-right: -52px; color: var(--ink-dark);
  }
  .address {
    position: absolute; right: 72px; top: 358px;
    text-align: right; font-size: 16px; line-height: 27px; color: var(--ink-light);
    white-space: nowrap;
  }
  .address__icon { position: absolute; right: 40px; top: 363px; width: 20px; height: 20px; }

  /* back */
  .back__disc {
    position: absolute; left: 300px; top: 32px; width: 240px; height: 240px; border-radius: 50%;
    background: var(--brand-yellow);
  }
  .back__name {
    position: absolute; left: 0; width: 100%; top: 308px; text-align: center;
    font-family: "Sniglet", "Open Sans", sans-serif;
    font-size: 46px; color: var(--kraft-pale); white-space: nowrap;
  }
  .web-tab {
    position: absolute; left: 448px; top: 392px; width: 355px; height: 77px;
    background: linear-gradient(180deg, var(--kraft-light) 0%, var(--kraft-pale) 45%, var(--kraft-light) 100%);
    clip-path: polygon(8% 0, 93% 0, 100% 45%, 100% 100%, 0 100%, 0 45%);
    display: flex; align-items: center; justify-content: center;
    font-size: 19px; color: var(--brand-blue); padding-top: 8px; white-space: nowrap;
  }
</style>
</head>
<body>
  <section class="card card--front" aria-label="Business card front">
    <div class="front__header"></div>
    <div class="front__band"></div>
    <div class="brand-dot"></div>
    <div class="brand-name">Gadgeteer Glowhaus</div>
    <p class="tagline">for your everyday techie<br>and beauty needs</p>
    <div class="name-tab"><span class="name-tab__text">Name</span></div>
    <p class="address">Gadgeteer Glowhaus R.J. Morrow 47, Wexcombe Avenue,<br>Ferndale Heights, Victoria 3187 Australia</p>
    <svg class="address__icon" viewBox="0 0 20 20" aria-hidden="true">
      <circle cx="10" cy="10" r="9.5" fill="#fff6e6"/>
      <path d="M4.5 10.5 L10 5 L15.5 10.5 H13.5 V15 H11 V12 H9 V15 H6.5 V10.5 Z" fill="#8a6231"/>
    </svg>
  </section>

  <section class="card card--back" aria-label="Business card back">
    <div class="back__disc"></div>
    <div class="back__name">Gadgeteer Glowhaus</div>
    <div class="web-tab">www.gadgeteerglowhaus.com</div>
  </section>
</body>
</html>
```